New Website Design for Rides for Heroes.org - A Site for People to Donate Cars to War / Disabled Ve

Current site: www.ridesforheroes.org; Look at these sites for ideas: bykes2tots.org; motorsfordreams.org; www.autosforourcadets.org; www.trucksforheroes.org

Industry/Entity Type

Charity

Coding

Coded - Design and coding required

Number of Pages Required

1 page

Requirements
Must have
• n/a
Nice to have
• n/a
Should not have
• n/a

```html
<!DOCTYPE html>
<html lang="en">
<head>
<meta charset="utf-8">
<title>Rides for Heroes – Donate Your Car</title>
<link href="https://fonts.googleapis.com/css2?family=Open+Sans:wght@400;600;700&display=swap" rel="stylesheet">
<style>
:root{
  --red:#d9261c;
  --red-dark:#b51c14;
  --blue:#1565c0;
  --blue-dark:#0d4f9e;
  --ink:#333;
  --muted:#666;
  --pale:#f3f7fc;
  --footer:#272b35;
  --white:#fff;
}
*{box-sizing:border-box;margin:0;padding:0}
html,body{width:1200px;height:2219px;overflow:hidden}
body{font-family:"Open Sans",Arial,sans-serif;color:var(--ink);background:var(--white);position:relative}
.wrap{width:1004px;margin:0 auto;position:relative}
a{color:inherit;text-decoration:none}

/* header */
.site-header{height:139px}
.site-header .wrap{height:139px;display:flex;align-items:center;justify-content:space-between}
.brand{display:flex;align-items:center;gap:10px;font-size:24px;font-weight:700;color:var(--red)}
.brand-mark{width:22px;height:22px;background:var(--red);border-radius:50%}
.header-actions{display:flex;gap:10px;align-items:center}
.help-box{width:218px;height:60px;border:1px solid #e2e2e2;border-radius:4px;background:#fafafa;padding:10px 0 0 24px;position:relative}
.help-box small{display:block;font-size:11px;color:var(--blue);font-weight:600}
.help-box strong{font-size:16px;font-weight:400;color:var(--red)}
.help-box .agent{position:absolute;right:14px;top:6px;width:46px;height:50px;border-radius:50% 50% 8px 8px;background:linear-gradient(#6b4a3a,#c9b3a6)}
.btn-donate{display:block;width:150px;height:56px;background:linear-gradient(var(--red),var(--red-dark));color:var(--white);font-size:14px;font-weight:700;text-align:center;line-height:56px;border-radius:4px}

/* nav */
.main-nav{height:55px;background:linear-gradient(var(--blue),var(--blue-dark))}
.main-nav ul{list-style:none;display:flex;height:55px}
.main-nav li{flex:1;text-align:center;line-height:55px;font-size:11px;color:var(--white);text-transform:uppercase}
.main-nav li.active{background:var(--red);flex:0 0 130px}

/* hero */
.hero{height:527px;position:relative;background:linear-gradient(180deg,#4f6b3a 0%,#7ea24c 50%,#8fb55a 100%)}
.hero-photo{position:absolute;inset:0}
.arrow{position:absolute;top:238px;width:36px;height:36px;border-radius:50%;background:rgba(80,90,60,.75)}
.arrow svg{display:block;margin:9px auto}
.arrow.prev{left:36px}.arrow.next{right:36px}
.donate-form{position:absolute;left:604px;top:84px;width:496px;height:356px;background:rgba(0,0,0,.78);border:2px solid rgba(255,255,255,.8);padding:22px 22px;color:var(--white)}
.donate-form h2{font-size:15px;font-weight:700;text-align:center}
.donate-form p{font-size:11.5px;text-align:center;margin-top:8px}
.donate-form p span{color:var(--red)}
.fields{display:grid;grid-template-columns:1fr 1fr;gap:12px 9px;margin-top:22px}
.field{height:34px;border:1px solid rgba(255,255,255,.8);font-size:11px;padding:0 10px;line-height:32px;position:relative}
.field.select::after{content:"";position:absolute;right:12px;top:12px;width:5px;height:5px;border-right:1px solid #fff;border-bottom:1px solid #fff;transform:rotate(45deg)}
.form-submit{margin-top:20px;height:42px;background:linear-gradient(var(--red),var(--red-dark));border-radius:4px;text-align:center;line-height:42px;font-size:13px;font-weight:700}

/* section headings */
.section-title{font-size:25px;font-weight:400;color:var(--blue);text-align:center;text-transform:uppercase}
.section-lead{font-size:13px;line-height:22px;color:var(--muted);text-align:center;margin:12px auto 0;width:920px}

/* steps */
.steps{height:448px;padding-top:37px}
.step-list{display:flex;margin-top:38px}
.step{flex:1;text-align:center;padding:0 12px;border-right:1px solid #e3e3e3}
.step:last-child{border-right:0}
.step-icon{width:138px;height:138px;border-radius:50%;border:1px solid;margin:0 auto;padding:6px}
.step-icon div{width:100%;height:100%;border-radius:50%;display:flex;align-items:center;justify-content:center}
.step.red .step-icon{border-color:var(--red)} .step.red .step-icon div{background:var(--red)}
.step.blue .step-icon{border-color:var(--blue)} .step.blue .step-icon div{background:var(--blue)}
.step h3{font-size:15px;font-weight:400;margin-top:16px;text-transform:uppercase}
.step.red h3,.step.red .more{color:var(--red)}
.step.blue h3,.step.blue .more{color:var(--blue)}
.step p{font-size:11.5px;line-height:22px;color:var(--muted);margin-top:6px}
.more{display:inline-block;font-size:11px;text-decoration:underline;margin-top:2px}

/* why */
.why{height:540px;background:var(--pale);padding-top:59px}
.why-card{background:var(--white);height:422px;box-shadow:0 0 6px rgba(0,0,0,.08);padding-top:26px}
.why-body{display:flex;margin:28px 0 0 17px}
.why-photo{width:446px;height:290px;background:linear-gradient(160deg,#c8a560 0%,#8a7a3a 45%,#5d6160 75%,#3d3f41 100%)}
.benefits{list-style:none;margin-left:39px;width:480px;border-right:6px solid #eef1f5;height:290px}
.benefits li{display:flex;gap:14px;margin-bottom:17px}
.tick{flex:0 0 34px;height:34px;border:1px solid #f0b5b2;border-radius:50%;display:flex;align-items:center;justify-content:center}
.benefits h4{font-size:14px;font-weight:400;color:var(--red)}
.benefits p{font-size:11.5px;line-height:21px;color:var(--muted);width:400px}

/* program */
.program{height:279px;background:linear-gradient(180deg,#2f6fc0 0%,#3d7fd0 60%,#2f6cbc 100%);color:var(--white);padding-top:42px}
.program .section-title{color:var(--white);font-size:18px}
.program .section-lead{color:var(--white);font-size:11.5px;width:920px}
.features{display:flex;gap:20px;margin-top:26px}
.feature{width:236px;height:82px;border:1px solid rgba(255,255,255,.75);display:flex;align-items:center;background:rgba(255,255,255,.06)}
.feature-icon{width:82px;height:80px;background:rgba(255,255,255,.22);display:flex;align-items:center;justify-content:center}
.feature span{font-size:14px;line-height:22px;padding-left:22px}

/* footer */
.site-footer{height:231px;background:var(--footer);color:#c8ccd4;padding-top:42px}
.footer-cols{display:flex}
.footer-col h5{font-size:14px;font-weight:400;color:var(--white);text-transform:uppercase;margin-bottom:16px}
.footer-col ul{list-style:none}
.footer-col li{font-size:11px;line-height:26px;padding-left:16px;position:relative}
.footer-col li::before{content:"";position:absolute;left:2px;top:11px;border-left:4px solid #999;border-top:3px solid transparent;border-bottom:3px solid transparent}
.badge{width:134px;height:50px;background:var(--white);border-radius:3px;margin-bottom:8px;display:flex;align-items:center;justify-content:center}
.badge i{display:block;width:34px;height:34px;border-radius:50%;background:#c5d3e3}
.badge i.sq{border-radius:4px;background:#d8d8d8;width:90px;height:28px}
.social{display:flex;gap:11px;margin-bottom:10px}
.social i{display:block;width:23px;height:23px;background:#8a8f99;border-radius:3px}
.copy{font-size:10.5px;color:var(--white)}
</style>
</head>
<body>

<header class="site-header">
  <div class="wrap">
    <a class="brand" href="#"><span class="brand-mark"></span>Rides for Heroes</a>
    <div class="header-actions">
      <div class="help-box"><small>WE NEED YOUR HELP</small><strong>1-800-555-0142</strong><span class="agent" role="img" aria-label="Support agent with headset"></span></div>
      <a class="btn-donate" href="#">DONATE NOW!</a>
    </div>
  </div>
</header>

<nav class="main-nav">
  <div class="wrap">
    <ul>
      <li class="active">Home</li><li>About us</li><li>How it works</li><li>Why us</li><li>FAQ</li><li>Donate a car</li><li>Contact us</li>
    </ul>
  </div>
</nav>

<section class="hero">
  <div class="hero-photo" role="img" aria-label="Veteran in a power wheelchair on a green meadow with trees behind"></div>
  <span class="arrow prev"><svg width="18" height="18" viewBox="0 0 18 18"><path d="M11 3 5 9l6 6" stroke="#fff" stroke-width="2.5" fill="none"/></svg></span>
  <span class="arrow next"><svg width="18" height="18" viewBox="0 0 18 18"><path d="M7 3l6 6-6 6" stroke="#fff" stroke-width="2.5" fill="none"/></svg></span>
  <form class="donate-form">
    <h2>DONATE YOUR CAR: FULL TAX DEDUCTION - RUNNING OR NOT</h2>
    <p>PLEASE FILL OUT FORM OR CALL TOLL-FREE <span>1-800-555-0142</span></p>
    <div class="fields">
      <div class="field">Name*</div><div class="field">E-mail*</div>
      <div class="field">Phone Number*</div><div class="field">Mobile Number*</div>
      <div class="field">Address*</div><div class="field">Cirty*</div>
      <div class="field select">State*</div><div class="field select">Zip Code*</div>
    </div>
    <div class="form-submit">CLICK HERE TO DONATE NOW!</div>
  </form>
</section>

<section class="steps">
  <div class="wrap">
    <h2 class="section-title">Donate your car</h2>
    <p class="section-lead">Consectetur adipiscing elit, sed do eiusmod tempor incididunt ut labore et dolore magna aliqua. Ut enim ad minim veniam, quis nostrud exercitation ullamco laboris nisi ut aliquip ex ea commodo consequat. Duis aute irure dolor</p>
    <div class="step-list">
      <div class="step red">
        <div class="step-icon"><div><svg width="46" height="46" viewBox="0 0 46 46" fill="none" stroke="#fff" stroke-width="3"><path d="M9 24v-4a14 14 0 0 1 28 0v4"/><rect x="6" y="22" width="7" height="11" rx="2" fill="#fff"/><rect x="33" y="22" width="7" height="11" rx="2" fill="#fff"/><circle cx="23" cy="25" r="9"/><path d="M36 33c0 5-5 7-10 7"/></svg></div></div>
        <h3>Call us</h3>
        <p>Rem aperiam, eaque ipsa quae ab illo inventore veritatis et quasi architecto beatae vitae dicta sunt explicabo. Nemo enim ipsam voluptatem quia</p>
        <a class="more" href="#">READ MORE</a>
      </div>
      <div class="step blue">
        <div class="step-icon"><div><svg width="56" height="50" viewBox="0 0 56 50" fill="#fff"><rect x="4" y="32" width="36" height="8"/><rect x="34" y="26" width="14" height="14"/><path d="M14 32 38 6l3 2-22 24z"/><path d="M38 6v14" stroke="#fff" stroke-width="2"/><circle cx="12" cy="43" r="4"/><circle cx="26" cy="43" r="4"/><circle cx="42" cy="43" r="4"/></svg></div></div>
        <h3>We tow it</h3>
        <p>Rem aperiam, eaque ipsa quae ab illo inventore veritatis et quasi architecto beatae vitae dicta sunt explicabo. Nemo enim ipsam voluptatem quia</p>
        <a class="more" href="#">READ MORE</a>
      </div>
      <div class="step blue">
        <div class="step-icon"><div><svg width="44" height="44" viewBox="0 0 44 44" fill="none" stroke="#fff" stroke-width="3"><path d="M26 8H10a4 4 0 0 0-4 4v22a4 4 0 0 0 4 4h22a4 4 0 0 0 4-4V20"/><path d="M34 5l5 5-16 16-7 2 2-7z"/></svg></div></div>
        <h3>Tax write-off</h3>
        <p>Rem aperiam, eaque ipsa quae ab illo inventore veritatis et quasi architecto beatae vitae dicta sunt explicabo. Nemo enim ipsam voluptatem quia</p>
        <a class="more" href="#">READ MORE</a>
      </div>
    </div>
  </div>
</section>

<section class="why">
  <div class="wrap">
    <div class="why-card">
      <h2 class="section-title">Why donate your car to us?</h2>
      <p class="section-lead">Consectetur adipiscing elit, sed do eiusmod tempor incididunt ut labore et dolore magna aliqua. Ut enim ad minim veniam, quis nostrud exercitation ullamco laboris nisi ut aliquip ex ea commodo consequat. Duis aute irure dolor</p>
      <div class="why-body">
        <div class="why-photo" role="img" aria-label="Black SUV parked on a road lined with autumn trees"></div>
        <ul class="benefits">
          <li><span class="tick"><svg width="16" height="16" viewBox="0 0 16 16"><path d="M3 8l3.5 3.5L13 4" stroke="#d9261c" stroke-width="2.2" fill="none"/></svg></span><div><h4>Free Local Towing</h4><p>We will pick up your car donation, running or not, when it's most convenient, at home or work...</p></div></li>
          <li><span class="tick"><svg width="16" height="16" viewBox="0 0 16 16"><path d="M3 8l3.5 3.5L13 4" stroke="#d9261c" stroke-width="2.2" fill="none"/></svg></span><div><h4>All Cars Accepted</h4><p>We take your car regardless of its condition or registration status.</p></div></li>
          <li><span class="tick"><svg width="16" height="16" viewBox="0 0 16 16"><path d="M3 8l3.5 3.5L13 4" stroke="#d9261c" stroke-width="2.2" fill="none"/></svg></span><div><h4>Income Tax Deduction</h4><p>We issue you an IRS tax receipt &amp; offer the largest resale network to get you the highest tax write-off possible.</p></div></li>
          <li><span class="tick"><svg width="16" height="16" viewBox="0 0 16 16"><path d="M3 8l3.5 3.5L13 4" stroke="#d9261c" stroke-width="2.2" fill="none"/></svg></span><div><h4>No Paperwork Hassles</h4><p>We take any car and handle everything: DMV, Smog and IRS paperwork.</p></div></li>
        </ul>
      </div>
    </div>
  </div>
</section>

<section class="program" role="region" aria-label="Car donation program over a soft city skyline">
  <div class="wrap">
    <h2 class="section-title">Car donation program</h2>
    <p class="section-lead">Consectetur adipiscing elit, sed do eiusmod tempor incididunt ut labore et dolore magna aliqua. Ut enim ad minim veniam, quis nostrud exercitation ullamco laboris nisi ut aliquip ex ea commodo consequat. Duis aute irure dolor</p>
    <div class="features">
      <div class="feature"><span class="feature-icon"><svg width="36" height="36" viewBox="0 0 36 36"><circle cx="18" cy="18" r="15" fill="#fff"/><path d="M10 12c4 0 5 4 8 4s2 6-2 7-3 5-6 3 0-6-2-8z" fill="#6d9bd6"/></svg></span><span>Donation Accepted<br>Nationwide</span></div>
      <div class="feature"><span class="feature-icon"><svg width="40" height="30" viewBox="0 0 40 30" fill="#fff"><path d="M6 14l5-10h18l5 10h2v10h-4v4h-5v-4H13v4H8v-4H4V14zm6 0h16l-3-6H15z"/></svg></span><span>All Vechile Types<br>Welcome</span></div>
      <div class="feature"><span class="feature-icon"><svg width="24" height="38" viewBox="0 0 24 38"><path d="M19 9c-2-2-4-3-7-3-4 0-7 2-7 5 0 7 14 4 14 12 0 3-3 6-7 6-3 0-6-1-8-4M12 2v34" stroke="#fff" stroke-width="3.5" fill="none"/></svg></span><span>Tax Deductible</span></div>
      <div class="feature"><span class="feature-icon"><svg width="36" height="36" viewBox="0 0 36 36" fill="#fff"><rect x="4" y="15" width="7" height="17"/><path d="M13 16l6-12c3 0 4 2 3 6l-1 4h9c2 0 3 2 2 4l-3 12c0 1-1 2-3 2H13z"/></svg></span><span>Towing is Free</span></div>
    </div>
  </div>
</section>

<footer class="site-footer">
  <div class="wrap footer-cols">
    <div class="footer-col" style="width:282px">
      <h5>Donate your car today!</h5>
      <ul><li>You have no costs.</li><li>Free towing, running or not.</li><li>We issue you an IRS tax receipt.</li><li>We take care of all paperwork.</li><li>And we take care of DMV &amp; Smog issues.</li></ul>
    </div>
    <div class="footer-col" style="width:197px">
      <h5>Safe &amp; secure</h5>
      <div class="badge"><i></i></div>
      <div class="badge"><i class="sq"></i></div>
    </div>
    <div class="footer-col" style="width:172px">
      <h5>Resources</h5>
      <ul><li>FAQ's</li><li>Tax Filing Info</li><li>Who we help</li><li>Vacation Voucher</li></ul>
    </div>
    <div class="footer-col" style="width:158px">
      <h5>Ways to give</h5>
      <ul><li>Donate Car</li><li>Donor Login</li><li>Agent Login</li><li>Contact us</li></ul>
    </div>
    <div class="footer-col">
      <h5>Connect with us</h5>
      <div class="social"><i></i><i></i><i></i><i></i><i></i></div>
      <p class="copy">COPYRIGHTS©2016 RIDESFORHEROES.</p>
    </div>
  </div>
</footer>

</body>
</html>
```